Property Management business needs Business cards designed

We provide a premium property management service based in Sydney's Norther Beaches. We want people to feel confident in choosing us to manage their investment properties. We offer a much more personalized service than other estate agents.
We want a modern clean design. Something that shows confidence without being complicated.
Logo attached.

Target Market(s)

35-70yo Male and Female with strong property portfolios within Sydney's Norther Beaches

Industry/Entity Type

Property Management

Contact Information for Business Card

Address: Suite 7, 12-14 Kelvin Parade, Harlow NSW 2188
Two separate named cards.
Tom Ardley - 0491 570 118 tom@harbourvaleestates.com.au
Clara Dunmore - 0491 570 263 clara@harbourvaleestates.com.au

Requirements
Must have
• Business logo, name, number, address, email.

```html
<!DOCTYPE html>
<html lang="en">
<head>
<meta charset="utf-8">
<title>Harbourvale Estates – Business Card</title>
<link href="https://fonts.googleapis.com/css2?family=Arimo:wght@400;700&display=swap" rel="stylesheet">
<style>
  :root {
    --page: #e9e9e7;
    --ink: #1b1b1d;
    --text-grey: #4a4a4c;
    --teal: #2a9aa0;
    --teal-light: #4fb9bd;
    --teal-dark: #1d7f85;
    --band-dark: #222326;
    --card-white: #ffffff;
    --card-fade: #d9d9db;
    --back-black: #141517;
    --back-sheen: #2c2e31;
    --back-text: #8d9094;
  }
  * { box-sizing: border-box; margin: 0; padding: 0; }
  html, body {
    width: 1200px; height: 950px; overflow: hidden;
    background: var(--page);
    font-family: "Arimo", Arial, sans-serif;
  }
  .canvas {
    width: 1200px; height: 950px;
    display: flex; flex-direction: column;
    align-items: center; justify-content: center; gap: 50px;
  }
  .card {
    position: relative;
    width: 700px; height: 400px;
    overflow: hidden;
    box-shadow: 0 6px 18px rgba(0,0,0,0.18);
  }

  /* Front */
  .card-front {
    background: linear-gradient(180deg, var(--card-white) 0%, var(--card-white) 55%, var(--card-fade) 100%);
  }
  .brand {
    position: absolute; left: 40px; top: 48px;
    display: flex; align-items: center; gap: 14px;
  }
  .brand-mark {
    width: 26px; height: 26px; border-radius: 50%;
    background: var(--teal);
  }
  .brand-name {
    font-weight: 700; font-size: 34px; letter-spacing: -0.5px;
    color: var(--ink); line-height: 1;
  }
  .name-band {
    position: absolute; left: 0; top: 138px;
    width: 100%; height: 44px;
    background: linear-gradient(90deg,
      var(--teal-dark) 0%, var(--teal) 30%, var(--teal-light) 55%, var(--teal) 62%,
      var(--band-dark) 62%, var(--band-dark) 100%);
  }
  .band-dot {
    position: absolute; right: 110px; top: 9px;
    width: 26px; height: 26px; border-radius: 50%;
    border: 3px solid var(--card-white);
  }
  .person-name {
    position: absolute; left: 40px; top: 0;
    line-height: 44px; font-size: 22px; color: var(--card-white);
  }
  .contact-list {
    position: absolute; left: 40px; top: 212px;
    list-style: none;
    font-size: 17px; line-height: 24px; color: var(--text-grey);
  }
  .address {
    position: absolute; right: 40px; bottom: 36px;
    font-style: normal; text-align: right;
    font-size: 19px; line-height: 26px; color: var(--text-grey);
  }

  /* Back */
  .card-back {
    background: linear-gradient(100deg, var(--back-black) 0%, var(--back-black) 62%, var(--back-sheen) 80%, var(--back-black) 100%);
  }
  .back-brand {
    position: absolute; left: 0; right: 0; top: 170px;
    display: flex; align-items: center; justify-content: center; gap: 14px;
  }
  .back-brand .brand-mark { background: var(--teal); }
  .back-brand .brand-name { color: var(--card-white); font-size: 30px; }
  .back-web {
    position: absolute; right: 40px; bottom: 40px;
    font-size: 16px; letter-spacing: 4px; color: var(--back-text);
  }
</style>
</head>
<body>
<main class="canvas">
  <section class="card card-front" aria-label="Business card front">
    <div class="brand">
      <span class="brand-mark"></span>
      <span class="brand-name">HARBOURVALE ESTATES</span>
    </div>
    <div class="name-band">
      <span class="person-name">Tom Ardley</span>
      <span class="band-dot"></span>
    </div>
    <ul class="contact-list">
      <li>0491 570 118</li>
      <li>tom@harbourvaleestates.com.au</li>
      <li>www.harbourvaleestates.com.au</li>
    </ul>
    <address class="address">
      Suite 7<br>
      12-14 Kelvin Parade<br>
      Harlow NSW 2188
    </address>
  </section>

  <section class="card card-back" aria-label="Business card back">
    <div class="back-brand">
      <span class="brand-mark"></span>
      <span class="brand-name">HARBOURVALE ESTATES</span>
    </div>
    <span class="back-web">www.harbourvaleestates.com.au</span>
  </section>
</main>
</body>
</html>
```